We need a web site design that is connected to Talbrook Roofing an American company, Veteran owned. Specializing in new roofs of all kinds, repair existing roofs and emergency roof repairs. located in the north Georgia mountains

Target Market(s)

homeowners end users, real estate, home owners insurance companies

Industry/Entity Type

roofing

Contact Information for Business Card

logo, Veteran owned, supports veteran charities, phone number ect

Font styles to use
Serif

Requirements
Should not have
• na

```html
<!DOCTYPE html>
<html lang="en">
<head>
<meta charset="UTF-8">
<title>Talbrook Roofing – Business Card</title>
<link href="https://fonts.googleapis.com/css2?family=Lora:wght@400;600;700&display=swap" rel="stylesheet">
<style>
  :root {
    --brand-red: #ed1c24;
    --paper: #ffffff;
    --faint-tint: rgba(237, 28, 36, 0.06);
    --faint-ring: rgba(230, 190, 120, 0.18);
  }
  html, body {
    margin: 0;
    padding: 0;
    overflow: hidden;
    background: var(--paper);
  }
  .card {
    position: relative;
    width: 1200px;
    height: 686px;
    overflow: hidden;
    background: var(--paper);
    font-family: "Lora", serif;
  }
  .backdrop-ring {
    position: absolute;
    left: 770px;
    top: 40px;
    width: 600px;
    height: 600px;
    border-radius: 50%;
    border: 10px solid var(--faint-ring);
    background: var(--faint-tint);
  }
  .brand-name {
    position: absolute;
    left: 0;
    width: 1200px;
    top: 140px;
    text-align: center;
    margin: 0;
    font-size: 48px;
    font-weight: 700;
    line-height: 1.2;
    color: var(--brand-red);
    letter-spacing: 1px;
  }
  .info-band {
    position: absolute;
    left: 0;
    top: 343px;
    width: 1200px;
    height: 326px;
    background: var(--brand-red);
    color: var(--paper);
  }
  .base-stripe {
    position: absolute;
    left: 0;
    top: 677px;
    width: 1200px;
    height: 9px;
    background: var(--brand-red);
  }
  .holder-name {
    position: absolute;
    left: 69px;
    top: 18px;
    margin: 0;
    font-size: 31px;
    font-weight: 700;
    line-height: 1.2;
  }
  .holder-name .underline {
    text-decoration: underline;
    text-decoration-thickness: 2px;
    text-underline-offset: 5px;
  }
  .holder-tagline {
    position: absolute;
    left: 69px;
    top: 58px;
    margin: 0;
    font-size: 21px;
    font-weight: 400;
    line-height: 1.2;
  }
  .contact-item {
    position: absolute;
    display: flex;
    align-items: center;
  }
  .contact-icon {
    flex: none;
    width: 48px;
    height: 48px;
    border-radius: 50%;
    background: var(--paper);
    display: flex;
    align-items: center;
    justify-content: center;
  }
  .contact-icon svg {
    width: 26px;
    height: 26px;
    fill: none;
    stroke: var(--brand-red);
    stroke-width: 1.6;
    stroke-linecap: round;
    stroke-linejoin: round;
  }
  .contact-text {
    line-height: 1.22;
    font-weight: 400;
  }
  .contact-phone { left: 69px; top: 130px; }
  .contact-phone .contact-text { margin-left: 24px; font-size: 32px; }
  .contact-address { left: 69px; top: 216px; align-items: flex-start; }
  .contact-address .contact-text { margin-left: 30px; font-size: 30px; line-height: 1.3; }
  .contact-web { left: 642px; top: 130px; }
  .contact-mail { left: 642px; top: 216px; }
  .contact-web .contact-text,
  .contact-mail .contact-text { margin-left: 28px; font-size: 36px; }
</style>
</head>
<body>
  <main class="card">
    <div class="backdrop-ring" aria-hidden="true"></div>
    <h1 class="brand-name">Talbrook Roofing</h1>

    <section class="info-band">
      <h2 class="holder-name"><span class="underline">Your</span> Name</h2>
      <p class="holder-tagline">Veteran owned &amp; operated</p>

      <div class="contact-item contact-phone">
        <span class="contact-icon">
          <svg viewBox="0 0 24 24"><path d="M5 3h3l2 5-2 1.5a11 11 0 0 0 6.5 6.5L16 14l5 2v3a2 2 0 0 1-2 2A17 17 0 0 1 3 5a2 2 0 0 1 2-2z"/><path d="M14 3a7 7 0 0 1 7 7"/><path d="M14 6.5a3.5 3.5 0 0 1 3.5 3.5"/></svg>
        </span>
        <span class="contact-text">+000 123 456 789</span>
      </div>

      <div class="contact-item contact-address">
        <span class="contact-icon">
          <svg viewBox="0 0 24 24"><path d="M12 22s-7-7.5-7-12.5a7 7 0 0 1 14 0C19 14.5 12 22 12 22z"/><circle cx="12" cy="9.5" r="2.6"/></svg>
        </span>
        <span class="contact-text">your street adress here<br>treet name 123</span>
      </div>

      <div class="contact-item contact-web">
        <span class="contact-icon">
          <svg viewBox="0 0 24 24"><circle cx="12" cy="12" r="9"/><ellipse cx="12" cy="12" rx="4" ry="9"/><path d="M3 12h18M4.5 7.5h15M4.5 16.5h15"/></svg>
        </span>
        <span class="contact-text">www.yourwebsite.com</span>
      </div>

      <div class="contact-item contact-mail">
        <span class="contact-icon">
          <svg viewBox="0 0 24 24"><rect x="3" y="5.5" width="18" height="13" rx="1.5"/><path d="M3.5 6.5l8.5 7 8.5-7"/></svg>
        </span>
        <span class="contact-text">yourmail@gmail.com</span>
      </div>
    </section>

    <div class="base-stripe" aria-hidden="true"></div>
  </main>
</body>
</html>
```